Frozen Yoghurt
Aufgabenstellung
Es soll eine Postkarte erstellt werden
auf die Vorteile des Produkts dargestellt werden
- kein fett (98% fettfrei)
- keine künstlichen süssungsmittel
- low calorien
- Viel Calcium
- Viel Eiweiss
- Vitamine durch Frucht topping
Die Postkarte soll gleichzeitig dazu dienen dass man sie mit zu uns ins Geschäft bringt und dann ein gratis Muster bekommt.
Mitbewerber: www.plumdrizzle.com, www.velvocup.com

```html
<!DOCTYPE html>
<html lang="de">
<head>
<meta charset="utf-8">
<title>Frozen Joghurt – Postkarte</title>
<link href="https://fonts.googleapis.com/css2?family=Barlow:wght@400;500;600&family=Kalam:wght@400&display=swap" rel="stylesheet">
<style>
  :root {
    --stage: #000000;
    --white: #ffffff;
    --green-dark: #17832c;
    --green-mid: #3aa535;
    --green-light: #8cc83a;
    --burst-red: #c8102e;
    --arrow-blue: #283a7a;
    --photo-dark: #3b2414;
    --photo-warm: #b06a2a;
    --photo-light: #e8d9c4;
    --ink: #111111;
  }
  * { box-sizing: border-box; margin: 0; padding: 0; }
  html, body { width: 1200px; height: 900px; overflow: hidden; background: var(--stage); }
  body { position: relative; font-family: "Barlow", Arial, sans-serif; color: var(--white); }

  /* ---------- Front card ---------- */
  .card-front {
    position: absolute; left: 60px; top: 120px; width: 450px; height: 660px;
    overflow: hidden; background: var(--green-mid);
  }
  .front-photo {
    position: absolute; left: 0; top: 0; width: 100%; height: 490px;
    background:
      radial-gradient(ellipse at 70% 75%, var(--photo-light) 0 22%, transparent 45%),
      radial-gradient(ellipse at 15% 40%, #e9c3a6 0 20%, transparent 40%),
      linear-gradient(160deg, var(--photo-dark) 0%, var(--photo-warm) 55%, #6b4a2c 100%);
  }
  .front-kicker {
    position: absolute; right: 36px; top: 26px;
    font-size: 27px; font-weight: 500; letter-spacing: 0.5px;
  }
  .front-headline {
    position: absolute; right: 32px; top: 78px; text-align: right;
    font-size: 52px; font-weight: 500; line-height: 1.08;
  }
  .front-band {
    position: absolute; left: 0; top: 490px; width: 100%; height: 170px;
    background: linear-gradient(100deg, var(--green-dark) 0%, var(--green-mid) 55%, var(--green-light) 100%);
    padding: 30px 80px 0 28px;
  }
  .front-band-title { font-size: 27px; font-weight: 500; line-height: 1.2; }
  .front-band-text { margin-top: 12px; font-size: 12px; line-height: 1.4; }
  .front-band-text strong { font-weight: 600; }
  .redeem-arrow { position: absolute; right: 0; top: 470px; width: 58px; height: 190px; }

  .burst { position: absolute; }
  .burst svg { display: block; width: 100%; height: 100%; }
  .burst-label {
    position: absolute; inset: 0; display: flex; flex-direction: column;
    align-items: center; justify-content: center; line-height: 1;
  }
  .burst-pct { font-weight: 500; }
  .burst-sub { font-weight: 500; }
  .card-front .burst { left: 195px; top: 380px; width: 130px; height: 130px; transform: rotate(-10deg); }
  .card-front .burst-pct { font-size: 27px; }
  .card-front .burst-sub { font-size: 13px; margin-top: 4px; }

  /* ---------- Back card ---------- */
  .card-back {
    position: absolute; left: 570px; top: 270px; width: 580px; height: 400px;
    overflow: hidden;
    background: linear-gradient(105deg, var(--green-dark) 0%, var(--green-mid) 45%, var(--green-light) 75%, var(--green-mid) 100%);
  }
  .back-photo {
    position: absolute; left: 0; top: 0; width: 255px; height: 140px;
    background:
      radial-gradient(ellipse at 30% 45%, #e4bfa1 0 24%, transparent 50%),
      linear-gradient(120deg, #a86a3a 0%, var(--photo-dark) 70%);
  }
  .back-kicker { position: absolute; left: 150px; top: 32px; font-size: 14px; font-weight: 500; }
  .card-back .burst { left: 150px; top: 60px; width: 95px; height: 95px; transform: rotate(-8deg); }
  .card-back .burst-pct { font-size: 21px; }
  .card-back .burst-sub { font-size: 10px; margin-top: 3px; }
  .back-offer { position: absolute; left: 0; top: 155px; width: 255px; text-align: center; }
  .back-offer-title { font-size: 40px; font-weight: 500; line-height: 1; }
  .back-offer-sub { margin-top: 8px; font-size: 20px; line-height: 1.25; }
  .cup-row { position: absolute; left: 22px; top: 270px; display: flex; gap: 14px; }
  .cup { width: 34px; height: 40px; border-radius: 40% 40% 6px 6px;
         background: linear-gradient(180deg, #f2ece4 0%, #b9435a 45%, #ffffff 60%, #e9e9e9 100%); }
  .back-benefits {
    position: absolute; left: 0; top: 325px; width: 255px; text-align: center;
    font-size: 11px; line-height: 1.35; color: var(--ink); font-weight: 500;
  }
  .divider { position: absolute; left: 270px; top: 40px; width: 3px; height: 330px;
             background: repeating-linear-gradient(180deg, var(--white) 0 60px, transparent 60px 72px); }
  .stamp-box { position: absolute; right: 28px; top: 28px; width: 60px; height: 68px; border: 2px solid var(--white); }
  .address { position: absolute; left: 300px; top: 170px; width: 250px; font-family: "Kalam", cursive; }
  .address-title { font-size: 17px; margin-bottom: 10px; }
  .address-line { font-size: 14px; padding: 10px 0 2px 4px; border-bottom: 1.5px solid rgba(255,255,255,0.85); }
</style>
</head>
<body>

<article class="card-front">
  <div class="front-photo" role="img" aria-label="Foto: junge Frau isst Frozen Joghurt mit Beeren und Granola aus einem Becher"></div>
  <p class="front-kicker">FROZEN JOGHURT</p>
  <h1 class="front-headline">Auf die Löffel,<br>fertig, los.</h1>
  <div class="burst">
    <svg viewBox="0 0 100 100" aria-hidden="true"><polygon fill="var(--burst-red)" points="100,50 89.6,60.6 93.3,75 79,79 75,93.3 60.6,89.6 50,100 39.4,89.6 25,93.3 21,79 6.7,75 10.4,60.6 0,50 10.4,39.4 6.7,25 21,21 25,6.7 39.4,10.4 50,0 60.6,10.4 75,6.7 79,21 93.3,25 89.6,39.4"/></svg>
    <div class="burst-label"><span class="burst-pct">100%</span><span class="burst-sub">Kalorienfrei</span></div>
  </div>
  <section class="front-band">
    <h2 class="front-band-title">GUTSCHEIN: Ein Gratis-<br>Becher Frozen Joghurt</h2>
    <p class="front-band-text"><strong>SO GEHT'S!</strong> Diese Karte mit zu uns in den Shop bringen (Adresse auf der Rückseite) und erhalten Sie einen Gratis-Becher Frozen Joghurt frei nach Wahl.</p>
  </section>
  <svg class="redeem-arrow" viewBox="0 0 58 190" aria-label="Jetzt Gutschein einlösen">
    <polygon points="10,0 58,95 10,190" fill="var(--arrow-blue)"/>
    <text x="0" y="0" transform="translate(30 95) rotate(-90)" text-anchor="middle" font-family="Barlow, sans-serif" font-size="7.5" font-weight="600" fill="#ffffff">JETZT GUTSCHEIN</text>
    <text x="0" y="0" transform="translate(39 95) rotate(-90)" text-anchor="middle" font-family="Barlow, sans-serif" font-size="7.5" font-weight="600" fill="#ffffff">EINLÖSEN</text>
  </svg>
</article>

<article class="card-back">
  <div class="back-photo" role="img" aria-label="Foto: junge Frau mit Löffel im Mund"></div>
  <p class="back-kicker">FROZEN JOGHURT</p>
  <div class="burst">
    <svg viewBox="0 0 100 100" aria-hidden="true"><polygon fill="var(--burst-red)" points="100,50 89.6,60.6 93.3,75 79,79 75,93.3 60.6,89.6 50,100 39.4,89.6 25,93.3 21,79 6.7,75 10.4,60.6 0,50 10.4,39.4 6.7,25 21,21 25,6.7 39.4,10.4 50,0 60.6,10.4 75,6.7 79,21 93.3,25 89.6,39.4"/></svg>
    <div class="burst-label"><span class="burst-pct">100%</span><span class="burst-sub">Kalorienfrei</span></div>
  </div>
  <div class="back-offer">
    <h2 class="back-offer-title">GRATIS!</h2>
    <p class="back-offer-sub">1 Frozen Joghurt<br>nach Wahl</p>
  </div>
  <div class="cup-row">
    <div class="cup" role="img" aria-label="Becher Frozen Joghurt mit Heidelbeeren"></div>
    <div class="cup" role="img" aria-label="Becher Frozen Joghurt mit Himbeeren"></div>
    <div class="cup" role="img" aria-label="Becher Frozen Joghurt mit Beerensauce"></div>
    <div class="cup" role="img" aria-label="Becher Frozen Joghurt mit Brombeeren"></div>
    <div class="cup" role="img" aria-label="Becher Frozen Joghurt mit Karamell"></div>
  </div>
  <p class="back-benefits">100% fettfrei<br>keine künstlichen Süssungsmittel<br>• Viel Calcium + Vitamine</p>

  <div class="divider"></div>
  <div class="stamp-box"></div>
  <div class="address">
    <p class="address-title">Gutschein einlösen bei:</p>
    <p class="address-line">Kornhaus Ecke</p>
    <p class="address-line">Cafebar Frischraum</p>
    <p class="address-line">Mühlegasse 12 – 14</p>
    <p class="address-line">3000 BERN</p>
  </div>
</article>

</body>
</html>
```